Health Information/Education Logo Design

We need a logo design for a new company based in Atlanta called Brightpath Care. The program is about patient empowerment. We provide health information and education on how to get healthy, stay healthy, and how to be proactive in your care. We also provide medication and injection training to help patients feel their best and to ensure successful therapy outcomes.
We like the colors yellow, pink, teal and purple and would like to see some or all of these colors in the designs. The final design should communicate caring, considerate, compassionate information, education and training services
Education
Contact Information for Business Card
Brightpath Care
Lorraine Pettaway RN, MSN, MHA
Nurse Educator
404.555.0187 cell
404.555.0142 fax

```html
<!DOCTYPE html>
<html lang="en">
<head>
<meta charset="utf-8">
<title>Brightpath Care – Business Card</title>
<link href="https://fonts.googleapis.com/css2?family=Arimo:wght@400&display=swap" rel="stylesheet">
<style>
  :root {
    --card-white: #ffffff;
    --brand-purple: #874b9c;
    --brand-pink: #e8a3c9;
    --text-light: #ffffff;
  }
  html, body {
    margin: 0;
    padding: 0;
    overflow: hidden;
    background: var(--card-white);
  }
  .business-card {
    position: relative;
    width: 1200px;
    height: 686px;
    overflow: hidden;
    background: var(--card-white);
    font-family: "Arimo", Arial, sans-serif;
  }
  .card-waves {
    position: absolute;
    inset: 0;
    width: 1200px;
    height: 686px;
  }
  .wave-pink { fill: var(--brand-pink); }
  .wave-purple { fill: var(--brand-purple); }

  .brand-name {
    position: absolute;
    right: 118px;
    top: 112px;
    margin: 0;
    font-size: 70px;
    font-weight: 400;
    letter-spacing: 1px;
    color: var(--brand-purple);
    line-height: 1;
    text-transform: lowercase;
  }
  .person {
    position: absolute;
    left: 105px;
    top: 316px;
    color: var(--brand-purple);
  }
  .person-name {
    margin: 0;
    font-size: 46px;
    font-weight: 400;
    line-height: 1.1;
  }
  .person-title {
    margin: 4px 0 0;
    font-size: 34px;
    font-weight: 400;
    line-height: 1.1;
  }
  .contact {
    position: absolute;
    top: 576px;
    margin: 0;
    font-size: 33px;
    color: var(--text-light);
    line-height: 1;
  }
  .contact-cell { left: 103px; }
  .contact-fax { right: 118px; }
</style>
</head>
<body>
<div class="business-card">
  <svg class="card-waves" viewBox="0 0 1050 600" preserveAspectRatio="none" aria-hidden="true">
    <path class="wave-pink" d="M0,448 C150,400 300,378 480,380 C650,382 720,395 850,370 C960,345 1020,270 1050,210 L1050,600 L0,600 Z"/>
    <path class="wave-purple" d="M0,448 C200,412 400,395 620,405 C760,412 860,400 940,370 C990,350 1030,320 1050,300 L1050,600 L0,600 Z"/>
  </svg>

  <h1 class="brand-name">Brightpath Care</h1>

  <div class="person">
    <p class="person-name">Lorraine Pettaway RN, MSN, MHA</p>
    <p class="person-title">Nurse Educator</p>
  </div>

  <p class="contact contact-cell">Cell.: 404.555.0187</p>
  <p class="contact contact-fax">Fax.: 404.555.0142</p>
</div>
</body>
</html>
```